Postcard Design

we are an environmentally safe cleaning company called Verdaplume Services, that specializes in post construction cleanup. for example, rehabbed houses and newly built commercial or residential space. we would like this mailer directed at the construction companies in order for them to call us before the property is ready to go to the buyer/client. we would like to see designs including a wood grain background and various earth toned colors (something very crisp, clean and not "flashy" marketing). It is important to convey we have flexibly with scheduling, competitive pricing, and that cleaning these properties not only enhances the contractors work but provides them with a happy customer. we are also on tobys board with a A rating and provide a 100% satisfaction guarentee

Industry/Entity Type

Construction

```html
<!DOCTYPE html>
<html lang="en">
<head>
<meta charset="utf-8">
<title>Verdaplume Services – Postcard</title>
<link rel="stylesheet" href="https://fonts.googleapis.com/css2?family=Montserrat:wght@500&family=Roboto+Condensed:ital,wght@1,400;1,700&display=swap">
<style>
  :root {
    --backdrop: #8cc84b;
    --card-white: #ffffff;
    --bar-green-dark: #1f7a34;
    --bar-green-light: #7cc242;
    --logo-grey: #2b2b2b;
    --wood-pale: #e0955a;
    --wood-light: #d4814a;
    --wood-mid: #bf6a34;
    --wood-deep: #a9541f;
    --wood-dark: #8f4217;
    --call-red: #b3141c;
    --call-red-dark: #8e0d14;
    --band-green-top: #8fd12a;
    --band-green-bottom: #2f8a1a;
    --band-yellow: #f3f04a;
    --leaf-light: #b4e85a;
    --leaf-dark: #3f9b1e;
    --badge-red: #a5161d;
    --badge-red-dark: #7e0f14;
    --text-white: #ffffff;
  }
  * { margin: 0; padding: 0; box-sizing: border-box; }
  html, body {
    width: 1200px;
    height: 832px;
    overflow: hidden;
    background: var(--backdrop);
  }
  .postcard {
    position: absolute;
    left: 88px;
    top: 48px;
    width: 1024px;
    height: 736px;
    overflow: hidden;
    background:
      linear-gradient(180deg,
        var(--card-white) 0%,
        var(--card-white) 24%,
        rgba(255,255,255,0.8) 33%,
        rgba(255,255,255,0.25) 42%,
        rgba(255,255,255,0) 50%),
      linear-gradient(180deg, rgba(0,0,0,0) 40%, rgba(90,30,5,0.18) 100%),
      linear-gradient(90deg,
        var(--wood-mid) 0%,
        var(--wood-light) 8%,
        var(--wood-deep) 14%,
        var(--wood-mid) 20%,
        var(--wood-pale) 28%,
        var(--wood-light) 34%,
        var(--wood-mid) 40%,
        var(--wood-deep) 46%,
        var(--wood-light) 53%,
        var(--wood-mid) 60%,
        var(--wood-pale) 66%,
        var(--wood-mid) 72%,
        var(--wood-deep) 80%,
        var(--wood-mid) 86%,
        var(--wood-dark) 93%,
        var(--wood-deep) 100%);
  }
  .top-bar {
    position: absolute;
    left: 0;
    top: 0;
    width: 100%;
    height: 43px;
    background: linear-gradient(90deg, var(--bar-green-dark) 0%, var(--bar-green-light) 65%, rgba(124,194,66,0.3) 100%);
  }
  .leaves {
    position: absolute;
    left: 664px;
    top: 0;
    width: 340px;
    height: 250px;
  }
  .leaves .leaf {
    position: absolute;
    border-radius: 50%;
    background: radial-gradient(ellipse at 45% 40%, var(--leaf-light) 0%, var(--leaf-dark) 85%);
  }
  .leaves .leaf-large {
    left: 10px;
    top: -10px;
    width: 230px;
    height: 130px;
    transform: rotate(-28deg);
  }
  .leaves .leaf-small {
    left: 200px;
    top: 110px;
    width: 150px;
    height: 100px;
    transform: rotate(32deg);
  }
  .brand-name {
    position: absolute;
    left: 50px;
    top: 152px;
    font-family: "Montserrat", sans-serif;
    font-weight: 500;
    font-size: 88px;
    line-height: 1;
    letter-spacing: -1px;
    color: var(--logo-grey);
  }
  .call-bar {
    position: absolute;
    left: 512px;
    top: 323px;
    width: 512px;
    height: 72px;
    background: linear-gradient(180deg, var(--call-red) 0%, var(--call-red-dark) 100%);
    display: flex;
    align-items: center;
    justify-content: center;
    font-family: "Roboto Condensed", sans-serif;
    font-style: italic;
    font-weight: 700;
    font-size: 44px;
    color: var(--text-white);
    text-shadow: 1px 2px 2px rgba(0,0,0,0.45);
  }
  .specialty-band {
    position: absolute;
    left: 203px;
    top: 405px;
    width: 821px;
    height: 115px;
    background: linear-gradient(180deg, var(--band-green-top) 0%, var(--band-green-bottom) 100%);
    padding: 10px 0 0 28px;
    font-family: "Roboto Condensed", sans-serif;
    font-style: italic;
    font-weight: 400;
    font-size: 36px;
    line-height: 48px;
    color: var(--text-white);
    text-shadow: 1px 1px 2px rgba(0,0,0,0.35);
  }
  .specialty-band .highlight { color: var(--band-yellow); }
  .rating-badge {
    position: absolute;
    left: 46px;
    top: 526px;
    width: 150px;
    height: 150px;
    transform: rotate(-14deg);
  }
  .benefits {
    position: absolute;
    left: 496px;
    top: 548px;
    list-style: none;
    font-family: "Roboto Condensed", sans-serif;
    font-style: italic;
    font-weight: 400;
    font-size: 36px;
    line-height: 47px;
    color: var(--text-white);
    text-shadow: 1px 1px 2px rgba(0,0,0,0.4);
  }
  .benefits li::before {
    content: "\2022";
    margin-right: 10px;
  }
</style>
</head>
<body>
  <main class="postcard">
    <div class="top-bar"></div>
    <div class="leaves" role="img" aria-label="Two fresh green leaves">
      <div class="leaf leaf-large"></div>
      <div class="leaf leaf-small"></div>
    </div>

    <h1 class="brand-name">Verdaplume</h1>

    <div class="call-bar">Call us at (555) 014-2368</div>

    <p class="specialty-band">
      Specializing in post construction cleanup of<br>
      <span class="highlight">rehabbed houses, commercial and residential spaces.</span>
    </p>

    <svg class="rating-badge" viewBox="0 0 150 150" role="img" aria-label="A rating on tobys board seal">
      <circle cx="75" cy="75" r="66" fill="var(--badge-red)"/>
      <circle cx="75" cy="75" r="68" fill="none" stroke="var(--badge-red)" stroke-width="12" stroke-dasharray="6 5"/>
      <circle cx="75" cy="75" r="58" fill="none" stroke="var(--badge-red-dark)" stroke-width="2" opacity="0.5"/>
    </svg>

    <ul class="benefits">
      <li>Flexible scheduling</li>
      <li>Competitive pricing</li>
      <li>100% Satisfaction Guarantee</li>
    </ul>
  </main>
</body>
</html>
```